Self Watering Planter Packaging

We would like to create a unique Retail Packaging for our Self Watering Planter.
It is a Cedar Planter that is a Self Watering Cedar Planter that has a fountain.
It has a long lasting battery that last 3 months watering every other day.
Programable Automatic Watering System
Fountain Oxygenates the water Keeping the fresh water flowing and prevents stagnate smelly water.
No more root Rot because the System Aerates the Roots every time you water. Just like it does in nature.
Patented System that waters from the bottom up
No Power Cords
No Solar Panels
No Plumbing
I have put the old packaging that we had for our first version. We want something much better than this. We want this to be slanted to urban living, and being able to grow anywhere,
This system is guaranteed to grow amazing plants, fruits and vegetables.
Packaging size will be 36"L x 4"x12"
We will want a matching sell sheet to go along with this as well.
Reason: I have extended the Deadline
Target Market(s)
Anyone that likes to garden but may not have the land to garden. Herb Gardens, Urban Gardens, etc.
Industry/Entity Type
Retail
Look and feel

```html
<!DOCTYPE html>
<html lang="en">
<head>
<meta charset="utf-8">
<title>Meadow Lane Grow Box – Packaging Layout</title>
<link href="https://fonts.googleapis.com/css2?family=Arimo:wght@400;700&family=Tinos&display=swap" rel="stylesheet">
<style>
  :root {
    --pack-green: #33cc33;
    --pack-lime: #ccff66;
    --frame-black: #000000;
    --badge-orange: #f5a833;
    --badge-yellow: #ffee00;
    --badge-red: #ee1111;
    --bullet-yellow: #ffee00;
    --ink: #111111;
    --label-ink: #222222;
    --guide-grey: #aaaaaa;
    --white: #ffffff;
  }
  html, body { margin: 0; padding: 0; overflow: hidden; }
  body { width: 1200px; height: 959px; background: var(--white); position: relative; font-family: "Arimo", Arial, sans-serif; }
  .abs { position: absolute; }

  .dim-label { position: absolute; font-size: 20px; line-height: 22px; color: var(--label-ink); }
  .guides { position: absolute; left: 0; top: 0; }

  .front-panel { left: 100px; top: 156px; width: 910px; height: 303px; background: var(--pack-green); }
  .hero-backing { left: 130px; top: 178px; width: 297px; height: 260px; background: var(--pack-lime); border-radius: 22px; }
  .hero-frame { left: 135px; top: 171px; width: 296px; height: 260px; background: var(--frame-black); border-radius: 22px; }
  .photo { position: absolute; }
  .hero-photo { left: 20px; top: 18px; width: 256px; height: 224px; background: linear-gradient(180deg, #7a6f9e 0%, #5f8a3a 40%, #c08a5a 55%, #a8744a 100%); border-radius: 8px; }

  .brand-name { left: 450px; top: 178px; width: 240px; color: var(--white); font-weight: 700; font-size: 27px; line-height: 32px; text-align: center; }
  .product-type { left: 450px; top: 272px; width: 240px; text-align: center; font-weight: 700; font-size: 15px; color: var(--ink); }

  .feature-list { left: 458px; top: 310px; width: 310px; margin: 0; padding: 0; list-style: none; font-family: "Tinos", "Times New Roman", serif; font-size: 10.5px; line-height: 12px; color: var(--ink); }
  .feature-list li { position: relative; padding-left: 23px; margin-bottom: 10px; text-align: justify; }
  .feature-list li::before { content: ""; position: absolute; left: 0; top: 1px; width: 10px; height: 10px; background: var(--bullet-yellow); box-shadow: 2px 2px 0 var(--ink); }

  .detail-frame { position: absolute; background: var(--frame-black); border-radius: 10px; box-shadow: 4px 4px 0 var(--frame-black); outline: 3px solid var(--pack-lime); }
  .detail-one { left: 690px; top: 172px; width: 172px; height: 128px; }
  .detail-two { left: 788px; top: 314px; width: 186px; height: 126px; }
  .detail-one .photo { left: 14px; top: 8px; width: 144px; height: 108px; background: linear-gradient(135deg, #6d8fbf 0%, #7a6a4a 50%, #9c7a50 100%); }
  .detail-two .photo { left: 14px; top: 8px; width: 158px; height: 108px; background: linear-gradient(135deg, #8fa860 0%, #5a5f66 50%, #3a2e22 100%); }

  .badge { position: absolute; left: 891px; width: 100px; height: 31px; border-radius: 50%; box-shadow: 3px 3px 0 var(--frame-black); font-size: 8px; font-weight: 700; display: flex; align-items: center; justify-content: center; }
  .badge-cords { top: 169px; background: var(--badge-orange); color: var(--white); }
  .badge-solar { top: 216px; background: var(--badge-yellow); color: var(--ink); }
  .badge-plumbing { top: 263px; background: var(--badge-red); color: var(--white); }

  .box-depth { position: absolute; left: 0; top: 0; }
  .depth-brand { font-family: "Arimo", Arial, sans-serif; font-weight: 700; font-size: 15px; fill: var(--white); }
  .depth-type { font-family: "Arimo", Arial, sans-serif; font-weight: 700; font-size: 6px; fill: var(--ink); }

  .side-panel { position: absolute; background: var(--pack-lime); }
  .side-inner { position: absolute; background: var(--pack-green); }
  .side-left { left: 12px; top: 540px; width: 103px; height: 301px; }
  .side-left .side-inner { left: 10px; top: 12px; width: 83px; height: 276px; }
  .side-right { left: 1077px; top: 545px; width: 101px; height: 300px; }
  .side-right .side-inner { left: 10px; top: 15px; width: 81px; height: 275px; }
  .side-mark { position: absolute; left: 50%; top: 50%; width: 220px; text-align: center; }
  .side-left .side-mark { transform: translate(-50%, -50%) rotate(-90deg); }
  .side-right .side-mark { transform: translate(-50%, -50%) rotate(90deg); }
  .side-brand { color: var(--white); font-weight: 700; font-size: 17px; line-height: 20px; }
  .side-type { font-weight: 700; font-size: 7px; color: var(--ink); margin-top: 3px; }

  .top-bottom-band { left: 140px; top: 554px; width: 904px; height: 100px; background: var(--pack-lime); }

  .panel-label { position: absolute; font-size: 20px; line-height: 24px; color: var(--ink); }
  .label-left { left: 156px; top: 707px; }
  .label-top { left: 464px; top: 715px; width: 260px; text-align: center; }
  .label-back { left: 464px; top: 773px; width: 280px; text-align: center; }
  .label-right { left: 934px; top: 717px; width: 100px; text-align: right; }
</style>
</head>
<body>

  <svg class="box-depth" width="1200" height="959" aria-hidden="true">
    <polygon class="box-top" points="100,156 188,92 1081,92 1010,156" fill="var(--pack-lime)"/>
    <polygon class="box-side" points="1010,156 1081,92 1081,388 1010,459" fill="var(--pack-lime)"/>
    <polygon class="box-side-inner" points="1022,144 1069,120 1069,402 1022,444" fill="var(--pack-green)"/>
    <g transform="translate(1046,280) skewY(-27) rotate(90)">
      <text class="depth-brand" x="0" y="-6" text-anchor="middle">Meadow Lane</text>
      <text class="depth-brand" x="0" y="10" text-anchor="middle">Grow Box</text>
      <text class="depth-type" x="0" y="20" text-anchor="middle">SELF WATERING PLANTER</text>
    </g>
  </svg>

  <svg class="guides" width="1200" height="959" aria-hidden="true">
    <line x1="78" y1="152" x2="186" y2="90" stroke="var(--label-ink)" stroke-width="1"/>
    <line x1="80" y1="156" x2="80" y2="458" stroke="var(--label-ink)" stroke-width="1"/>
    <line x1="106" y1="486" x2="1006" y2="486" stroke="var(--guide-grey)" stroke-width="2"/>
    <polygon points="121,739 144,681 144,798" fill="var(--ink)"/>
    <polygon points="592,665 504,702 681,702" fill="var(--ink)"/>
    <polygon points="1062,739 1041,681 1041,798" fill="var(--ink)"/>
  </svg>

  <div class="dim-label" style="left:110px;top:96px;">4"</div>
  <div class="dim-label" style="left:64px;top:292px;background:var(--white);">12"</div>
  <div class="dim-label" style="left:540px;top:475px;background:var(--white);padding:0 4px;">36"</div>

  <section class="abs front-panel"></section>
  <div class="abs hero-backing"></div>
  <div class="abs hero-frame">
    <div class="photo hero-photo" role="img" aria-label="Photo of the cedar planter on legs filled with flowering herbs and grasses"></div>
  </div>

  <div class="abs brand-name">Meadow Lane<br>Grow Box</div>
  <div class="abs product-type">SELF WATERING PLANTER</div>

  <ul class="abs feature-list">
    <li>It is a Cedar Planter that is a Self Watering Cedar Planter that has a fountain. It has a long lasting battery that last 3 months watering every other day.</li>
    <li>Programable Automatic Watering System Fountain Oxygenates the water Keeping the fresh water flowing and prevents stagnate smelly water.</li>
    <li>No more root Rot because the System Aerates the Roots every time you water. Just like it does in nature.</li>
    <li>Patented System that waters from the bottom up</li>
  </ul>

  <div class="detail-frame detail-one">
    <div class="photo" role="img" aria-label="Close-up of the planter with the central fountain reservoir"></div>
  </div>
  <div class="detail-frame detail-two">
    <div class="photo" role="img" aria-label="Close-up of the fountain water flowing inside the planter"></div>
  </div>

  <div class="badge badge-cords">NO POWER CORDS</div>
  <div class="badge badge-solar">NO SOLAR PANELS</div>
  <div class="badge badge-plumbing">NO PLUMBING</div>

  <div class="side-panel side-left">
    <div class="side-inner">
      <div class="side-mark">
        <div class="side-brand">Meadow Lane<br>Grow Box</div>
        <div class="side-type">SELF WATERING PLANTER</div>
      </div>
    </div>
  </div>

  <div class="abs top-bottom-band"></div>

  <div class="side-panel side-right">
    <div class="side-inner">
      <div class="side-mark">
        <div class="side-brand">Meadow Lane<br>Grow Box</div>
        <div class="side-type">SELF WATERING PLANTER</div>
      </div>
    </div>
  </div>

  <div class="panel-label label-left">LEFT<br>SIDE</div>
  <div class="panel-label label-top">TOP and BOTTOM</div>
  <div class="panel-label label-back">BACK same with FRONT</div>
  <div class="panel-label label-right">RIGHT<br>SIDE</div>

</body>
</html>
```